Stationary and design update for my brand

I need new letterhead, a new business card, business envelope design, new keynote and powerpoint branded slides (16x9). I have logo samples in various styles and brand standards for fonts and colors.

Font styles to use
Sans Serif

```html
<!DOCTYPE html>
<html lang="en">
<head>
<meta charset="utf-8">
<title>Ridgeline Stationery and Slides</title>
<link href="https://fonts.googleapis.com/css2?family=Montserrat:wght@700;800&family=Roboto:wght@400;500;700&display=swap" rel="stylesheet">
<style>
:root{
  --orange:#F7941D;
  --grey:#808080;
  --ink:#555;
  --muted:#8a8a8a;
  --paper:#fff;
  --board-top:#e4e4e6;
  --board-bottom:#c9cacd;
}
*{margin:0;padding:0;box-sizing:border-box}
html,body{width:918px;height:1200px;overflow:hidden}
body{position:relative;font-family:'Roboto',sans-serif;color:var(--ink);background:var(--board-bottom)}
.board-top{position:absolute;left:0;top:0;width:918px;height:647px;background:var(--board-top)}
.piece{position:absolute;background:var(--paper);box-shadow:0 3px 6px rgba(0,0,0,.25);overflow:hidden}
.abs{position:absolute}
.brand{font-family:'Roboto',sans-serif;font-weight:500;color:var(--orange);letter-spacing:.06em;line-height:1}
.brand.white{color:#fff}
.center{text-align:center;left:0;right:0}
.stripe{position:absolute;left:0;width:100%}
.contact{display:flex;align-items:center;gap:3px;white-space:nowrap}
.contact svg{flex:none}
/* business card */
.card-name{font-weight:700;color:var(--orange);font-size:7px}
.card-role{font-size:4.4px;color:var(--muted)}
.card-line{font-size:4.6px;color:var(--ink);justify-content:center}
/* slides */
.slide{width:273px;height:153px}
.slide-title{font-family:'Montserrat',sans-serif;font-weight:800;color:var(--orange);font-size:10.5px;left:15px;top:15px;white-space:nowrap}
.slide-logo{right:8px;top:9px;font-size:6px}
.slide-foot{left:0;right:0;bottom:8px;height:6px}
.slide-foot span{position:absolute;left:7px;top:0;font-size:3.6px;color:var(--orange)}
.slide-foot i{position:absolute;left:16px;right:0;top:2.5px;border-top:.5px solid var(--orange)}
.t{font-size:3.1px;line-height:1.35;color:var(--muted)}
.t.w{color:#fff}
.h{font-size:6.2px;font-weight:500;color:var(--ink)}
.ho{font-size:5.3px;font-weight:500;color:var(--orange)}
.num{font-family:'Montserrat',sans-serif;font-weight:700;color:var(--orange);font-size:7px}
.photo{position:absolute;border:1px solid #ccc}
.phone{position:absolute;width:31px;height:62px;border:1.2px solid #222;border-radius:4px;background:#fff}
.phone::before{content:"";position:absolute;left:9px;top:0;width:11px;height:2.5px;background:#222;border-radius:0 0 2px 2px}
.avatar{position:absolute;width:24px;height:24px;border-radius:50%;border:1.5px solid #fff;background:linear-gradient(#d9d9d9,#9d9d9d)}
.member{position:absolute;width:60px;text-align:center;color:#fff}
.member b{display:block;font-family:'Montserrat',sans-serif;font-size:4.8px;font-weight:700}
.icon-dot{position:absolute;width:20px;height:20px;border-radius:50%;background:var(--grey);border:1.5px solid #fff;box-shadow:0 0 0 1px #bbb}
</style>
</head>
<body>
<div class="board-top"></div>

<!-- business card front -->
<section class="piece" style="left:41px;top:44px;width:197px;height:118px" aria-label="Business card front">
  <div class="abs center brand" style="top:24px;font-size:17px">RIDGELINE</div>
  <div class="abs center card-name" style="top:62px">Daniel Harrow-Pryce, DMIN, PCC</div>
  <div class="abs center card-role" style="top:71px">Owner / Trainer / Coach / Consultant</div>
  <div class="abs center contact card-line" style="top:82px">
    <svg width="6" height="6" viewBox="0 0 10 10"><rect width="10" height="10" rx="1.5" fill="#F7941D"/><path d="M3 2.2l1.2 1.6-.7.8c.5 1 1.2 1.7 2.1 2.1l.8-.7 1.6 1.2-.8 1C5 8 2.2 5.1 2 3z" fill="#fff"/></svg>
    <span>(555) 210-4819</span>&nbsp;
    <svg width="6" height="6" viewBox="0 0 10 10"><rect width="10" height="10" rx="1.5" fill="#F7941D"/><rect x="2" y="3" width="6" height="4.2" fill="none" stroke="#fff" stroke-width=".8"/><path d="M2 3l3 2.4L8 3" fill="none" stroke="#fff" stroke-width=".8"/></svg>
    <span>daniel@ridgelinecbc.com</span>
  </div>
  <div class="abs center card-line" style="top:92px;font-size:4.6px;text-align:center">4820 Alder Crest Rd. Plano, TX 75024</div>
  <svg class="stripe" style="top:104px" width="197" height="4" viewBox="0 0 197 4"><polygon points="0,1 118,1 116,4 0,4" fill="#F7941D"/><polygon points="118,0 197,0 197,3 116,3" fill="#808080"/></svg>
</section>

<!-- business card back -->
<section class="piece" style="left:259px;top:44px;width:197px;height:118px;background:var(--orange)" aria-label="Business card back">
  <div class="abs center brand white" style="top:52px;font-size:24px">RIDGELINE</div>
</section>

<!-- envelope back -->
<section class="piece" style="left:41px;top:180px;width:415px;height:208px" aria-label="Envelope back">
  <svg class="abs" style="left:0;top:0" width="415" height="47" viewBox="0 0 415 47"><path d="M0 0H415L408 34Q405 46 392 46H23Q10 46 7 34Z" fill="#F7941D"/></svg>
  <div class="abs center brand white" style="top:20px;font-size:15px">RIDGELINE</div>
</section>

<!-- envelope front -->
<section class="piece" style="left:41px;top:403px;width:415px;height:208px" aria-label="Envelope front">
  <div class="abs brand" style="left:14px;top:30px;font-size:19px">RIDGELINE</div>
  <div class="abs" style="left:15px;top:167px;font-size:6.4px;font-weight:500;color:#555">Ridgeline Coaching and Behavioral Consulting LLC</div>
  <div class="abs contact" style="left:15px;top:177px;font-size:5.5px">
    <svg width="6.5" height="6.5" viewBox="0 0 10 10"><rect width="10" height="10" rx="1.5" fill="#F7941D"/><path d="M5 1.8a2.3 2.3 0 0 1 2.3 2.3C7.3 6 5 8.4 5 8.4S2.7 6 2.7 4.1A2.3 2.3 0 0 1 5 1.8z" fill="#fff"/><circle cx="5" cy="4.1" r=".9" fill="#F7941D"/></svg>
    <span>4820 Alder Crest Rd. Plano, TX 75024</span>
  </div>
  <svg class="stripe" style="top:190px" width="415" height="4" viewBox="0 0 415 4"><polygon points="0,1 218,1 216,4 0,4" fill="#F7941D"/><polygon points="218,0 415,0 415,3 216,3" fill="#808080"/></svg>
</section>

<!-- letterhead -->
<section class="piece" style="left:471px;top:44px;width:405px;height:567px" aria-label="Letterhead">
  <div class="abs brand" style="left:13px;top:28px;font-size:18px">RIDGELINE</div>
  <div class="abs contact" style="left:57px;top:528px;font-size:7px">
    <svg width="8" height="8" viewBox="0 0 10 10"><rect width="10" height="10" rx="1.5" fill="#F7941D"/><path d="M3 2.2l1.2 1.6-.7.8c.5 1 1.2 1.7 2.1 2.1l.8-.7 1.6 1.2-.8 1C5 8 2.2 5.1 2 3z" fill="#fff"/></svg>
    <span>(555) 210-4819</span>&nbsp;&nbsp;
    <svg width="8" height="8" viewBox="0 0 10 10"><rect width="10" height="10" rx="1.5" fill="#F7941D"/><rect x="2" y="3" width="6" height="4.2" fill="none" stroke="#fff" stroke-width=".8"/><path d="M2 3l3 2.4L8 3" fill="none" stroke="#fff" stroke-width=".8"/></svg>
    <span>daniel@ridgelinecbc.com</span>&nbsp;&nbsp;
    <svg width="8" height="8" viewBox="0 0 10 10"><rect width="10" height="10" rx="1.5" fill="#F7941D"/><path d="M5 1.8a2.3 2.3 0 0 1 2.3 2.3C7.3 6 5 8.4 5 8.4S2.7 6 2.7 4.1A2.3 2.3 0 0 1 5 1.8z" fill="#fff"/><circle cx="5" cy="4.1" r=".9" fill="#F7941D"/></svg>
    <span>4820 Alder Crest Rd. Plano, TX 75024</span>
  </div>
  <svg class="stripe" style="top:546px" width="405" height="4" viewBox="0 0 405 4"><polygon points="0,1 208,1 206,4 0,4" fill="#F7941D"/><polygon points="208,0 405,0 405,3 206,3" fill="#808080"/></svg>
</section>

<!-- slide 1 cover -->
<section class="piece slide" style="left:41px;top:672px;background:var(--orange)" aria-label="Cover slide">
  <div class="abs center brand white" style="top:66px;font-size:26px">RIDGELINE</div>
  <div class="abs" style="left:12px;top:125px;font-size:5px;color:#fff">PRESENTATION</div>
  <div class="abs" style="left:12px;top:131px;color:#fff;white-space:nowrap"><b style="font-family:Montserrat,sans-serif;font-size:9px">BUSINESS</b> <span style="font-size:7px;font-weight:500">MARKETING</span></div>
  <div class="abs" style="left:112px;right:0;top:138px;border-top:.7px solid #fff"></div>
</section>

<!-- slide 2 contents -->
<section class="piece slide" style="left:322px;top:672px" aria-label="Contents slide">
  <div class="abs slide-title" style="left:22px;top:15px;font-size:13px">CONTENTS</div>
  <div class="abs brand slide-logo">RIDGELINE</div>
  <div class="abs" style="left:33px;top:43px;width:220px;display:grid;grid-template-columns:1fr 1fr;row-gap:12px;column-gap:10px">
    <div style="display:flex;gap:4px"><span class="num">1.</span><div><div class="h">Lorem ipsum</div><div class="t">Lorem ipsum dolor sit amet, consectetuer adipiscing elit, sed diam nonummy nibh</div></div></div>
    <div style="display:flex;gap:4px"><span class="num">2.</span><div><div class="h">Lorem ipsum</div><div class="t">Lorem ipsum dolor sit amet, consectetuer adipiscing elit, sed diam nonummy nibh euismod</div></div></div>
    <div style="display:flex;gap:4px"><span class="num">3.</span><div><div class="h">Lorem ipsum</div><div class="t">Lorem ipsum dolor sit amet, consectetuer adipiscing elit, sed diam nonummy nibh</div></div></div>
    <div style="display:flex;gap:4px"><span class="num">4.</span><div><div class="h">Lorem ipsum</div><div class="t">Lorem ipsum dolor sit amet, consectetuer adipiscing elit, sed diam nonummy nibh euismod</div></div></div>
    <div style="display:flex;gap:4px"><span class="num">5.</span><div><div class="h">Lorem ipsum</div><div class="t">Lorem ipsum dolor sit amet, consectetuer adipiscing elit, sed diam nonummy nibh</div></div></div>
    <div style="display:flex;gap:4px"><span class="num">6.</span><div><div class="h">Lorem ipsum</div><div class="t">Lorem ipsum dolor sit amet, consectetuer adipiscing elit, sed diam nonummy nibh euismod</div></div></div>
  </div>
  <div class="abs slide-foot"><span>02</span><i></i></div>
</section>

<!-- slide 3 about -->
<section class="piece slide" style="left:603px;top:672px" aria-label="About slide">
  <div class="abs slide-title" style="top:12px">ABOUT US COMPANY</div>
  <div class="abs brand slide-logo">RIDGELINE</div>
  <div class="abs" style="left:0;top:35px;width:150px;height:95px;background:var(--orange)"></div>
  <div class="abs t w" style="left:15px;top:40px;width:118px">Lorem ipsum dolor sit amet, consectetuer adipiscing elit, sed diam nonummy nibh euismod tincidunt ut laoreet dolore magna aliquam erat volutpat. Ut wisi enim ad minim veniam, quis nostrud exerci tation ullamcorper suscipit lobortis nisl ut aliquip ex ea commodo consequat. Duis autem vel eum iriure dolor in hendrerit in vulputate velit esse molestie consequat, vel illum dolore eu feugiat nulla facilisis at vero eros et accumsan et iusto odio dignissim qui blandit praesent luptatum zzril delenit augue duis dolore te feugait nulla facilisi.<br><br>Lorem ipsum dolor sit amet, cons ectetuer adipiscing elit, sed diam nonummy nibh euismod tincidunt ut laoreet dolore magna aliquam erat volutpat. Ut wisi enim ad</div>
  <div class="icon-dot" style="left:138px;top:41px"></div>
  <div class="icon-dot" style="left:138px;top:71px"></div>
  <div class="icon-dot" style="left:138px;top:104px"></div>
  <div class="abs" style="left:167px;top:41px;width:100px"><div class="ho">Lorem ipsum</div><div class="t" style="color:#555">ipsum dolor sit amet, cons ectetuer adipiscing elit, sed diam nonummy nibh euismod tincidunt ut laoreet</div></div>
  <div class="abs" style="left:166px;top:71px;width:100px"><div class="ho">Lorem ipsum</div><div class="t" style="color:#555">ipsum dolor sit amet, cons ectetuer adipiscing elit, sed diam nonummy nibh euismod tincidunt ut laoreet dolore magna aliquam erat volutpat.</div></div>
  <div class="abs" style="left:166px;top:104px;width:100px"><div class="ho">Lorem ipsum</div><div class="t" style="color:#555">ipsum dolor sit amet, cons ectetuer adipiscing elit, sed diam nonummy nibh euismod tincidunt</div></div>
  <div class="abs slide-foot"><span>03</span><i></i></div>
</section>

<!-- slide 4 overview -->
<section class="piece slide" style="left:41px;top:837px" aria-label="Company overview slide">
  <div class="abs slide-title" style="top:12px">COMPANY OVERVIEW</div>
  <div class="abs brand slide-logo">RIDGELINE</div>
  <div class="abs t" style="left:15px;top:31px;width:110px">Lorem ipsum dolor sit amet, consectetuer adipiscing elit, sed diam nonummy nibh euismod tincidunt ut laoreet dolore magna aliquam erat volutpat. Ut wisi enim ad minim veniam, quis nostrud exerci tation ullamcorper suscipit lobortis nisl ut aliquip ex ea commodo consequat. Duis autem vel eum iriure dolor in hendrerit<br><br>Lorem ipsum dolor sit amet, consectetuer adipiscing elit, sed diam nonummy nibh euismod tincidunt ut laoreet dolore magna aliquam erat volutpat. Ut wisi enim ad minim veniam, quis nostrud exerci tation ullamcorper suscipit lobortis nisl ut aliquip ex ea commodo</div>
  <svg class="abs" style="left:135px;top:32px" width="135" height="50" viewBox="0 0 135 50" font-family="Roboto,sans-serif" font-size="2.6" fill="#555">
    <g stroke="#ddd" stroke-width=".3"><line x1="12" y1="3" x2="132" y2="3"/><line x1="12" y1="10" x2="132" y2="10"/><line x1="12" y1="17" x2="132" y2="17"/><line x1="12" y1="24" x2="132" y2="24"/><line x1="12" y1="31" x2="132" y2="31"/><line x1="12" y1="38" x2="132" y2="38"/></g>
    <line x1="12" y1="45" x2="132" y2="45" stroke="#999" stroke-width=".4"/>
    <text x="2" y="4">60</text><text x="2" y="11">50</text><text x="2" y="18">40</text><text x="2" y="25">30</text><text x="2" y="32">20</text><text x="2" y="39">10</text><text x="5" y="46">0</text>
    <polyline points="16,44 28,38 40,25 52,34 64,19 76,29 88,26 100,22 112,18" fill="none" stroke="#808080" stroke-width=".7"/>
    <polyline points="16,44 28,42 40,30 52,15 64,20 76,31 88,24 100,18 112,35" fill="none" stroke="#F7941D" stroke-width=".7"/>
    <text x="13" y="49">TEXT 01</text><text x="37" y="49">TEXT 03</text><text x="61" y="49">TEXT 05</text><text x="85" y="49">TEXT 07</text><text x="109" y="49">TEXT 09</text>
  </svg>
  <svg class="abs" style="left:15px;top:82px" width="110" height="55" viewBox="0 0 110 55" font-family="Roboto,sans-serif" font-size="3" fill="#555">
    <g stroke="#ddd" stroke-width=".3"><line x1="8" y1="3" x2="107" y2="3"/><line x1="8" y1="11" x2="107" y2="11"/><line x1="8" y1="19" x2="107" y2="19"/><line x1="8" y1="27" x2="107" y2="27"/><line x1="8" y1="35" x2="107" y2="35"/><line x1="8" y1="43" x2="107" y2="43"/></g>
    <line x1="8" y1="50" x2="107" y2="50" stroke="#999" stroke-width=".4"/>
    <text x="0" y="4">60</text><text x="0" y="12">50</text><text x="0" y="20">40</text><text x="0" y="28">30</text><text x="0" y="36">20</text><text x="0" y="44">10</text><text x="2" y="51">0</text>
    <rect x="15" y="17" width="3" height="33" fill="#F7941D"/><rect x="19" y="8" width="3" height="42" fill="#808080"/>
    <rect x="37" y="41" width="3" height="9" fill="#808080"/><rect x="41" y="22" width="3" height="28" fill="#F7941D"/>
    <rect x="59" y="39" width="3" height="11" fill="#808080"/><rect x="63" y="2" width="3" height="48" fill="#808080"/><rect x="67" y="39" width="3" height="11" fill="#F7941D"/>
    <rect x="85" y="7" width="3" height="43" fill="#F7941D"/><rect x="89" y="25" width="3" height="25" fill="#808080"/>
    <text x="16" y="55">JAN</text><text x="38" y="55">FEB</text><text x="60" y="55">MAR</text><text x="84" y="55">APR</text>
  </svg>
  <div class="abs" style="left:140px;top:98px;width:125px;display:grid;grid-template-columns:1fr 1fr;row-gap:7px;column-gap:6px">
    <div style="display:flex;gap:3px"><svg width="4" height="4"><circle cx="2" cy="2" r="2" fill="#F7941D"/></svg><div><div class="ho" style="font-size:4.2px">Lorem ipsum</div><div class="t" style="font-size:2.6px">Lorem ipsum dolor sit amet, consectetuer adipiscing elit, sed diam nonummy nibh euismod</div></div></div>
    <div style="display:flex;gap:3px"><svg width="4" height="4"><circle cx="2" cy="2" r="2" fill="#F7941D"/></svg><div><div class="ho" style="font-size:4.2px">Lorem ipsum</div><div class="t" style="font-size:2.6px">Lorem ipsum dolor sit amet, consectetuer adipiscing elit, sed diam nonummy nibh euismod</div></div></div>
    <div style="display:flex;gap:3px"><svg width="4" height="4"><circle cx="2" cy="2" r="2" fill="#F7941D"/></svg><div><div class="ho" style="font-size:4.2px">Lorem ipsum</div><div class="t" style="font-size:2.6px">Lorem ipsum dolor sit amet, consectetuer adipiscing elit, sed diam nonummy nibh euismod</div></div></div>
    <div style="display:flex;gap:3px"><svg width="4" height="4"><circle cx="2" cy="2" r="2" fill="#F7941D"/></svg><div><div class="ho" style="font-size:4.2px">Lorem ipsum</div><div class="t" style="font-size:2.6px">Lorem ipsum dolor sit amet, consectetuer adipiscing elit, sed diam nonummy nibh euismod</div></div></div>
  </div>
  <div class="abs slide-foot"><span>04</span><i></i></div>
</section>

<!-- slide 5 project -->
<section class="piece slide" style="left:322px;top:837px" aria-label="Project slide">
  <div class="abs slide-title" style="left:11px;top:12px">LOREM IPSUM PROJECT</div>
  <div class="abs brand slide-logo">RIDGELINE</div>
  <div class="abs t" style="left:11px;top:33px;width:230px">Lorem ipsum dolor sit amet, consectetuer adipiscing elit, sed diam nonummy nibh euismod tincidunt ut laoreet dolore magna aliquam erat volutpat. Ut wisi enim ad minim veniam, quis nostrud exerci tation ullamcorper suscipit lobortis nisl utea commodo consequat. Duis autem vel eum iriure dolor in hendrerit<br><br>Lorem ipsum dolor sit amet, consectetuer adipiscing elit, sed diam nonummy nibh m ipsum dolor sit amet, consectetuer adipiscing elit, sed diam nonummy nibh euismod tincidunt ut laoreet dolore magna.</div>
  <div class="photo" style="left:11px;top:70px;width:58px;height:40px;background:linear-gradient(135deg,#2c3e55,#6f8aa6)" role="img" aria-label="Photo: hand touching a glowing screen"></div>
  <div class="photo" style="left:75px;top:70px;width:58px;height:40px;background:linear-gradient(135deg,#d8dde2,#8e99a4)" role="img" aria-label="Photo: business team meeting at a table"></div>
  <div class="photo" style="left:139px;top:70px;width:58px;height:40px;background:linear-gradient(135deg,#0b2a5a,#3d7ecf)" role="img" aria-label="Photo: digital interface in blue light"></div>
  <div class="photo" style="left:203px;top:70px;width:58px;height:40px;background:linear-gradient(135deg,#143244,#4a8c9c)" role="img" aria-label="Photo: technology data visual"></div>
  <div class="abs" style="left:11px;top:112px;width:58px"><div class="ho">Lorem ipsum</div><div class="t" style="font-size:2.6px">Lorem ipsum dolor sit amet, consectetuer adipiscing elit, sed diam nonummy nibh euismod tincidunt ut laoreet</div></div>
  <div class="abs" style="left:75px;top:112px;width:58px"><div class="ho">Lorem ipsum</div><div class="t" style="font-size:2.6px">Lorem ipsum dolor sit amet, consectetuer adipiscing elit, sed diam nonummy nibh euismod tincidunt ut laoreet</div></div>
  <div class="abs" style="left:139px;top:112px;width:58px"><div class="ho">Lorem ipsum</div><div class="t" style="font-size:2.6px">Lorem ipsum dolor sit amet, consectetuer adipiscing elit, sed diam nonummy nibh euismod tincidunt ut laoreet</div></div>
  <div class="abs" style="left:203px;top:112px;width:58px"><div class="ho">Lorem ipsum</div><div class="t" style="font-size:2.6px">Lorem ipsum dolor sit amet, consectetuer adipiscing elit, sed diam nonummy nibh euismod tincidunt ut laoreet</div></div>
  <div class="abs slide-foot"><span>05</span><i></i></div>
</section>

<!-- slide 6 intelligence -->
<section class="piece slide" style="left:603px;top:837px" aria-label="Active intelligence slide">
  <div class="abs slide-title" style="left:10px;top:10px">ACTIVE INTELLIGENCE</div>
  <div class="abs brand slide-logo">RIDGELINE</div>
  <div class="abs t" style="left:10px;top:33px;width:125px;text-align:justify">Lorem ipsum dolor sit amet, consectetuer adipiscing elit, sed diam nonummy nibh euismod tincidunt ut laoreet dolore magna aliquam erat volutpat. Ut wisi enim ad minim veniam, quis nostrud exerci tation ullamcorper suscipit lobortis nisl ut aliquip ex ea commodo consequat. Duis autem vel eum iriure dolor in hendrerit in vulputate velit esse<br><br>Lorem ipsum dolor sit amet, consectetuer adipiscing elit, sed diam nonummy nibh euismod tincidunt ut laoreet dolore magna aliquam erat volutpat. Ut wisi enim ad minim veniam, quis nostrud exerci tation ullamcorper suscipit lobortis nisl ut aliquip ex ea commodo consequat. Duis autem vel eum iriure dolor in hendrerit in vulputate velit esse</div>
  <svg class="abs" style="left:12px;top:99px" width="4" height="4" viewBox="0 0 4 4"><polygon points="0,0 4,2 0,4" fill="#F7941D"/></svg>
  <div class="abs t" style="left:22px;top:98px;width:105px">Lorem ipsum dolor sit amet, consectetuer adipiscing elit, sed diam nonummy nibh euismod tincidunt ut laoreet dolore magna</div>
  <svg class="abs" style="left:12px;top:117px" width="4" height="4" viewBox="0 0 4 4"><polygon points="0.3,0.3 3.6,2 0.3,3.7" fill="none" stroke="#F7941D" stroke-width=".5"/></svg>
  <div class="abs t" style="left:22px;top:116px;width:105px">Lorem ipsum dolor sit amet, consectetuer adipiscing elit, sed diam nonummy nibh euismod tincidunt ut laoreet dolore magna</div>
  <div class="abs" style="left:197px;top:32px;width:60px;border-top:1px solid var(--orange)"></div>
  <div class="abs" style="left:140px;top:60px;height:80px;border-left:1px solid var(--orange)"></div>
  <div class="abs" style="left:140px;top:139px;width:60px;border-top:1px solid var(--orange)"></div>
  <div class="photo" style="left:143px;top:34px;width:130px;height:102px;border:none;background:linear-gradient(120deg,#e9e4dc,#b7a493 60%,#8a7463)" role="img" aria-label="Photo: colleagues gathered around a laptop"></div>
  <div class="abs slide-foot"><span>06</span><i></i></div>
</section>

<!-- slide 7 use cases -->
<section class="piece slide" style="left:41px;top:1003px" aria-label="Use cases slide">
  <div class="abs slide-title" style="top:10px">USE CASES</div>
  <div class="abs brand slide-logo">RIDGELINE</div>
  <div class="abs t" style="left:15px;top:31px;width:112px;text-align:justify">Lorem ipsum dolor sit amet, consectetuer adipiscing elit, sed diam nonummy nibh euismod tincidunt ut laoreet dolore magna aliquam erat volutpat. Ut wisi enim ad minim veniam, quis nostrud exerci tation ullamcorper suscipit lobortis nisl ut aliquip ex ea commodo consequat. Duis autem vel eum iriure dolor in hendrerit<br><br>Lorem ipsum dolor sit amet, consectetuer adipiscing elit, sed diam nonummy nibh euismod tincidunt ut laoreet dolore magna aliquam erat volutpat. Ut wisi enim ad minim veniam, quis nostrud exerci tation ullamcorper suscipit lobortis nisl ut aliquip ex ea commodo consequat. Duis autem vel eum iriure dolor in hendrerit in hendrerit in aliquam erat volutpat. Ut wisi enim ad minim veniam, quis nostrud exerci tation ullamcorper suscipit lobortis nisl ut aliquip ex ea commodo consequat. Duis autem vel eum iriure dolor in hendrerit in</div>
  <div class="phone" style="left:136px;top:28px">
    <div class="abs ho" style="left:3px;top:10px;font-size:3.8px;line-height:1.1">Lorem<br>ipsum dolor</div>
    <div class="abs t" style="left:3px;top:34px;width:24px;font-size:2px">To introduce the solutions to the changing landscape of marketing and equip them with knowledge</div>
  </div>
  <div class="phone" style="left:176px;top:48px">
    <div class="abs ho" style="left:3px;top:12px;font-size:3.8px;line-height:1.1">Dolor sit<br>amet, conse</div>
    <div class="abs t" style="left:3px;top:38px;width:24px;font-size:2px">You will learn concepts and ideas in digital marketing as well as how to use tools</div>
  </div>
  <div class="phone" style="left:216px;top:70px">
    <div class="abs ho" style="left:3px;top:15px;font-size:3.8px">Consec</div>
    <div class="abs t" style="left:3px;top:40px;width:24px;font-size:2px">You are required to pass 80% of the evaluation test to obtain the certificate</div>
  </div>
  <div class="abs slide-foot"><span>07</span><i></i></div>
</section>

<!-- slide 8 team -->
<section class="piece slide" style="left:322px;top:1003px" aria-label="Team slide">
  <div class="abs slide-title" style="left:14px;top:14px">TEAM MEMBERS AND ADVISORS</div>
  <div class="abs brand slide-logo">RIDGELINE</div>
  <div class="abs t" style="left:14px;top:35px;width:215px">Lorem ipsum dolor sit amet, consectetuer adipiscing elit, sed diam nonummy nibh euismod tincidunt ut laoreet dolore magna aliquam erat volutpat. Ut wisi enim ad minim veniam, quis nostrud exerci tation ullamcorper suscipit lobortis nisl ut aliquip ex ea commodo consequat. Duis autem<br><br>Lorem ipsum dolor sit amet, cons ectetuer adipiscing elit, sed diam nonummy nibh euismod tincidunt ut laoreet dolore magna aliquam erat volutpat.</div>
  <div class="abs" style="left:0;right:0;top:68px;height:60px;background:var(--orange)"></div>
  <div class="avatar" style="left:23px;top:71px" role="img" aria-label="Portrait of team member"></div>
  <div class="avatar" style="left:92px;top:71px" role="img" aria-label="Portrait of team member"></div>
  <div class="avatar" style="left:158px;top:71px" role="img" aria-label="Portrait of team member"></div>
  <div class="avatar" style="left:226px;top:71px" role="img" aria-label="Portrait of team member"></div>
  <div class="member" style="left:5px;top:98px"><b>JOHN SMITH</b><div class="t w" style="font-size:2.3px">ipsum dolor sit amet, cons ectetuer adipiscing elit, sed diam nonummy nibh euismod tincidunt ut laoreet</div></div>
  <div class="member" style="left:74px;top:98px"><b>MILLIE SMITH</b><div class="t w" style="font-size:2.3px">ipsum dolor sit amet, cons ectetuer adipiscing elit, sed diam nonummy nibh euismod tincidunt ut laoreet</div></div>
  <div class="member" style="left:140px;top:98px"><b>JOHN SMITH</b><div class="t w" style="font-size:2.3px">ipsum dolor sit amet, cons ectetuer adipiscing elit, sed diam nonummy nibh euismod tincidunt ut laoreet</div></div>
  <div class="member" style="left:208px;top:98px"><b>MILLIE SMITH</b><div class="t w" style="font-size:2.3px">ipsum dolor sit amet, cons ectetuer adipiscing elit, sed diam nonummy nibh euismod tincidunt ut laoreet</div></div>
  <div class="abs slide-foot"><span>08</span><i></i></div>
</section>

<!-- slide 9 closing -->
<section class="piece slide" style="left:603px;top:1003px" aria-label="Closing slide">
  <div class="abs center brand" style="top:50px;font-size:28px">RIDGELINE</div>
  <div class="abs" style="left:0;right:0;top:97px;height:14px;background:var(--orange);color:#fff;font-size:8px;font-weight:500;text-align:center;line-height:14px">Ridgeline Coaching and Behavioral Consulting LLC</div>
  <div class="abs center contact" style="top:118px;justify-content:center;font-size:7px">
    <svg width="8" height="8" viewBox="0 0 10 10"><rect width="10" height="10" rx="1.5" fill="#F7941D"/><path d="M3 2.2l1.2 1.6-.7.8c.5 1 1.2 1.7 2.1 2.1l.8-.7 1.6 1.2-.8 1C5 8 2.2 5.1 2 3z" fill="#fff"/></svg>
    <span>(555) 210-4819</span>&nbsp;&nbsp;
    <svg width="8" height="8" viewBox="0 0 10 10"><rect width="10" height="10" rx="1.5" fill="#F7941D"/><rect x="2" y="3" width="6" height="4.2" fill="none" stroke="#fff" stroke-width=".8"/><path d="M2 3l3 2.4L8 3" fill="none" stroke="#fff" stroke-width=".8"/></svg>
    <span>daniel@ridgelinecbc.com</span>
  </div>
  <div class="abs center" style="top:131px;font-size:7px;text-align:center">4820 Alder Crest Rd. Plano, TX 75024</div>
</section>
</body>
</html>
```